Corbett Architecture (business card)

We need a business card design. We are a full service architectural firm that specializes in mostly residential projects and some commercial projects. We are located in Hudson Valley, New York. We work with high end clients and want a business card that is memorable and has a sleek, modern, design but will not go out of style (timeless).

Target Market(s)

high end residential clients

Industry/Entity Type

Architect

Contact Information for Business Card

Front of card
Company Logo
website: www.corbettdesignstudo.example
what we do: residential, Commercial

back of card
Owner's Name: Martin Corbett
owner's title: Principal
Business address: 2867 Orchard Lane Suite B, Maplethorpe, NY 10938
phone number: 845-555-0192
e-mail: mc@corbettdesignstudio.example

We like:
icons
sleek and clean design
simple not too busy or too much text

Font styles to use
Sans Serif

Colors
0356a4

Requirements
Must have
• company colors are navy blue, white, and gray
• Front of card
• Company Logo
• website: www.corbettdesignstudo.example
• what we do: residential, Commercial
• back of card
• Owner's Name: Martin Corbett
• owner's title: Principal
• Business address: 2867 Orchard Lane Suite B, Maplethorpe, NY 10938
• phone number: 845-555-0192
• e-mail: mc@corbettdesignstudio.example
Nice to have
• We like:
• icons
• sleek and clean design
• simple not too much text
• color of the card to be either blue or gray
Should not have
• we do not like houses in the design or plans of houses-this is over done and we don't like it.
• no QR CODES

```html
<!DOCTYPE html>
<html lang="en">
<head>
<meta charset="utf-8">
<title>Corbett Architecture – Business Card</title>
<link href="https://fonts.googleapis.com/css2?family=Lato:wght@400;700;900&display=swap" rel="stylesheet">
<style>
  :root {
    --navy: #221c69;
    --navy-deep: #1a1556;
    --white: #ffffff;
    --ink: #1c1b2e;
    --stage: #2c2f33;
  }
  * { margin: 0; padding: 0; box-sizing: border-box; }
  html, body { width: 1200px; height: 900px; overflow: hidden; }
  body {
    background: var(--stage);
    font-family: "Lato", sans-serif;
    position: relative;
  }
  .card {
    position: absolute;
    width: 520px;
    height: 300px;
    top: 300px;
  }
  /* Contact side */
  .card-back {
    left: 50px;
    background: var(--white);
    border: 7px solid var(--navy);
    display: flex;
    align-items: center;
    padding: 0 24px 0 20px;
  }
  .identity {
    width: 190px;
    text-align: right;
    padding-right: 16px;
    align-self: center;
    margin-top: -40px;
  }
  .person-name {
    color: var(--navy);
    font-weight: 700;
    font-size: 22px;
    line-height: 1.1;
  }
  .person-title {
    color: var(--ink);
    font-size: 15px;
    margin-top: 2px;
  }
  .divider {
    width: 5px;
    height: 92px;
    background: var(--navy);
    margin-right: 14px;
    align-self: center;
    margin-top: -20px;
  }
  .contact-list { list-style: none; margin-top: 20px; }
  .contact-item {
    display: flex;
    align-items: flex-start;
    gap: 10px;
    color: var(--ink);
    font-size: 13.5px;
    line-height: 1.3;
    margin-bottom: 6px;
  }
  .contact-item svg { width: 16px; height: 16px; flex: none; fill: var(--navy); margin-top: 1px; }
  /* Brand side */
  .card-front {
    left: 630px;
    background: linear-gradient(160deg, var(--navy) 0%, var(--navy-deep) 100%);
    color: var(--white);
  }
  .frame {
    position: absolute;
    inset: 20px;
    border: 1.5px solid var(--white);
  }
  .brand {
    position: absolute;
    top: 92px;
    left: 0; right: 0;
    text-align: center;
  }
  .brand-name {
    font-weight: 900;
    font-size: 27px;
    letter-spacing: 0.5px;
  }
  .brand-services {
    font-size: 10.5px;
    letter-spacing: 3.5px;
    margin-top: 6px;
  }
  .brand-web {
    position: absolute;
    bottom: 48px;
    left: 0; right: 0;
    text-align: center;
    font-size: 13px;
    font-weight: 700;
  }
</style>
</head>
<body>
  <section class="card card-back">
    <div class="identity">
      <div class="person-name">Martin Corbett</div>
      <div class="person-title">Principal</div>
    </div>
    <div class="divider"></div>
    <ul class="contact-list">
      <li class="contact-item">
        <svg viewBox="0 0 24 24" aria-hidden="true"><path d="M6.6 10.8a15.1 15.1 0 0 0 6.6 6.6l2.2-2.2c.3-.3.7-.4 1-.2 1.1.4 2.3.6 3.6.6.6 0 1 .4 1 1V20c0 .6-.4 1-1 1A17 17 0 0 1 3 4c0-.6.4-1 1-1h3.5c.6 0 1 .4 1 1 0 1.3.2 2.5.6 3.6.1.3 0 .7-.2 1z"/></svg>
        <span>845-555-0192</span>
      </li>
      <li class="contact-item">
        <svg viewBox="0 0 24 24" aria-hidden="true"><path d="M2 5h20v14H2z M2 5l10 8 10-8" fill="none" stroke="#221c69" stroke-width="2"/><path d="M2 5l10 8 10-8z"/></svg>
        <span>mc@corbettdesignstudio.example</span>
      </li>
      <li class="contact-item">
        <svg viewBox="0 0 24 24" aria-hidden="true"><g fill="none" stroke="#221c69" stroke-width="1.8"><circle cx="12" cy="12" r="9.5"/><ellipse cx="12" cy="12" rx="4" ry="9.5"/><path d="M2.5 12h19M4 7h16M4 17h16"/></g></svg>
        <span>www.corbettdesignstudo.example</span>
      </li>
      <li class="contact-item">
        <svg viewBox="0 0 24 24" aria-hidden="true"><path d="M12 2a7 7 0 0 0-7 7c0 5 7 13 7 13s7-8 7-13a7 7 0 0 0-7-7zm0 9.5A2.5 2.5 0 1 1 12 6.5a2.5 2.5 0 0 1 0 5z"/></svg>
        <span>2867 Orchard Lane Suite B,<br>Maplethorpe, NY 10938</span>
      </li>
    </ul>
  </section>

  <section class="card card-front">
    <div class="frame"></div>
    <div class="brand">
      <div class="brand-name">CORBETT ARCHITECTURE</div>
      <div class="brand-services">RESIDENTIAL COMMERCIAL</div>
    </div>
    <div class="brand-web">www.corbettdesignstudo.example</div>
  </section>
</body>
</html>
```